Real Estate Sign - For Sale Yard Sign - Willowmere Estates

Our real estate company is looking for a new sign design to hang from in post in the front yard of the homes we are selling. Our company name is Willowmere Estates and we are open to any ideas. Attached for you is our company logo and name. The font is Trajan Pro. We are looking for a classy sign to put in front of our high end more expensive homes. You can either choose to include or not include the words "FOR SALE" on the sign (in our state, only about 1/2 of the real estate signs have room for those words. It is implied with a sign in the yard in front of a home). Thank you.

24 inches wide is important. and the height should be either 18, 24 or 30 inches. For printing purposes either of those heights will work. 18 inches is common, but some signs look great that are taller too. I'm open.

If you have any ideas for some better text options, styles or fonts, feel free to play with it.

P.S. Please feel free to play with the colors. We are not at this point set on a particular color scheme. Colors we think are nice but you may have other better ideas are black, red, white, gold, green

Target Market(s)

High end real estate home owners who choose to use our company to sell their home.

Industry/Entity Type

Real Estate

Requirements
Must have
• Company Logo
Company Name (Willowmere Estates)
Barnaby Follwick (please include my name as I am the real estate agent)
503-618-3940 (my phone number for potential clients to contact me)
Website name - willowmereestatesnw.example
***You can either choose to include the words "FOR SALE" or not***

Dimensions must be 24 inches wide. Height can be either 18, 24 or 30 inches. Must be one of those 3 heights for printing purposes.

```html
<!DOCTYPE html>
<html lang="en">
<head>
<meta charset="utf-8">
<title>Willowmere Estates – Yard Sign</title>
<link rel="stylesheet" href="https://fonts.googleapis.com/css2?family=Cinzel:wght@400&family=Poiret+One&display=swap">
<style>
  :root {
    --paper: #ffffff;
    --frame-brown: #8c7a6b;
    --panel-slate: #79888a;
    --panel-edge: #bcc2cf;
    --sage: #c6d7b8;
    --sage-dash: #a9c59d;
    --ornament: #b3b8c6;
    --ink-light: #f3f3f1;
  }
  html, body {
    margin: 0;
    padding: 0;
    width: 1200px;
    height: 900px;
    overflow: hidden;
    background: var(--paper);
  }
  .yard-sign {
    display: block;
    width: 1200px;
    height: 900px;
  }
  .sign-backer { fill: var(--frame-brown); }
  .stitch-line {
    fill: none;
    stroke: var(--sage-dash);
    stroke-width: 2;
    stroke-dasharray: 6 5;
  }
  .sign-panel {
    fill: var(--panel-slate);
    stroke: var(--panel-edge);
    stroke-width: 4;
  }
  .corner-ornament { fill: var(--ornament); opacity: 0.85; }
  .brand-mark { fill: var(--sage); }
  .brand-name {
    font-family: "Cinzel", "Trajan Pro", serif;
    font-weight: 400;
    fill: var(--ink-light);
  }
  .brand-name--primary { font-size: 122px; }
  .brand-name--secondary { font-size: 58px; }
  .divider-dot, .divider-bar { fill: var(--sage); }
  .agent-detail {
    font-family: "Poiret One", sans-serif;
    fill: var(--ink-light);
  }
  .agent-name { font-size: 46px; }
  .agent-phone { font-size: 54px; }
  .agent-web { font-size: 52px; }
  .contact-icon { fill: var(--sage); }
  .contact-icon-line {
    fill: none;
    stroke: var(--sage);
    stroke-width: 3;
  }
</style>
</head>
<body>
<svg class="yard-sign" viewBox="0 0 1200 900" xmlns="http://www.w3.org/2000/svg">
  <!-- backer board -->
  <rect class="sign-backer" x="40" y="30" width="1125" height="845"/>

  <!-- dashed stitching around the panel -->
  <path class="stitch-line" d="M68,150 H290 C380,78 820,78 910,150 H1140 V835 H690 Q600,850 510,835 H68 Z"/>

  <!-- corner ornaments -->
  <path class="corner-ornament" role="img" aria-label="Scrollwork ornament, top left corner"
        d="M100,135 C100,105 120,78 150,72 C160,58 185,58 192,74 C215,70 228,90 245,100 C268,108 290,115 300,135 Z"/>
  <path class="corner-ornament" role="img" aria-label="Scrollwork ornament, top right corner"
        d="M1105,135 C1105,105 1085,78 1055,72 C1045,58 1020,58 1013,74 C990,70 977,90 960,100 C937,108 915,115 900,135 Z"/>

  <!-- main panel -->
  <path class="sign-panel"
        d="M102,135 H300 C385,62 815,62 900,135 H1103 Q1115,135 1115,147 V816 Q1115,828 1103,828 H700 Q600,842 500,828 H102 Q90,828 90,816 V147 Q90,135 102,135 Z"/>

  <!-- brand mark -->
  <circle class="brand-mark" cx="600" cy="205" r="62"/>

  <!-- company name -->
  <text class="brand-name brand-name--primary" x="600" y="410" text-anchor="middle"
        textLength="775" lengthAdjust="spacingAndGlyphs">WILLOWMERE</text>
  <text class="brand-name brand-name--secondary" x="605" y="480" text-anchor="middle"
        textLength="680" lengthAdjust="spacingAndGlyphs">ESTATES REAL ESTATE</text>

  <!-- divider -->
  <g class="divider">
    <circle class="divider-dot" cx="277" cy="535" r="4.5"/>
    <circle class="divider-dot" cx="292" cy="535" r="4.5"/>
    <circle class="divider-dot" cx="307" cy="535" r="4.5"/>
    <circle class="divider-dot" cx="322" cy="535" r="4.5"/>
    <circle class="divider-dot" cx="337" cy="535" r="4.5"/>
    <circle class="divider-dot" cx="352" cy="535" r="4.5"/>
    <circle class="divider-dot" cx="367" cy="535" r="4.5"/>
    <circle class="divider-dot" cx="382" cy="535" r="4.5"/>
    <circle class="divider-dot" cx="397" cy="535" r="4.5"/>
    <circle class="divider-dot" cx="412" cy="535" r="4.5"/>
    <rect class="divider-bar" x="425" y="528" width="355" height="14" rx="6"/>
    <circle class="divider-dot" cx="793" cy="535" r="4.5"/>
    <circle class="divider-dot" cx="808" cy="535" r="4.5"/>
    <circle class="divider-dot" cx="823" cy="535" r="4.5"/>
    <circle class="divider-dot" cx="838" cy="535" r="4.5"/>
    <circle class="divider-dot" cx="853" cy="535" r="4.5"/>
    <circle class="divider-dot" cx="868" cy="535" r="4.5"/>
    <circle class="divider-dot" cx="883" cy="535" r="4.5"/>
    <circle class="divider-dot" cx="898" cy="535" r="4.5"/>
    <circle class="divider-dot" cx="913" cy="535" r="4.5"/>
    <circle class="divider-dot" cx="928" cy="535" r="4.5"/>
  </g>

  <!-- agent contact -->
  <text class="agent-detail agent-name" x="582" y="643" text-anchor="middle">Barnaby Follwick</text>

  <g class="phone-icon">
    <rect class="contact-icon" x="327" y="662" width="28" height="52" rx="7"/>
    <rect x="333" y="672" width="16" height="14" rx="2" fill="var(--panel-slate)"/>
    <circle cx="341" cy="700" r="3.5" fill="var(--panel-slate)"/>
  </g>
  <text class="agent-detail agent-phone" x="402" y="715">503-618-3940</text>

  <g class="web-icon">
    <circle class="contact-icon-line" cx="183" cy="763" r="17"/>
    <ellipse class="contact-icon-line" cx="183" cy="763" rx="7" ry="17"/>
    <line class="contact-icon-line" x1="166" y1="763" x2="200" y2="763"/>
    <path class="contact-icon" d="M188,766 L188,790 L194,784 L199,793 L203,791 L198,782 L206,781 Z"/>
  </g>
  <text class="agent-detail agent-web" x="238" y="784"
        textLength="730" lengthAdjust="spacingAndGlyphs">willowmereestatesnw.example</text>
</svg>
</body>
</html>
```